TR Advisory Business Cards - High End AV / Low Voltage Company

We are low voltage AV company that specializes in high end clients on the residential side and larger businesses on the commercial side. We want something modern, tech looking but also something that is extremely professional looking. We have uploaded our logos and postcards we already have in the field. Along with a picture of one of our wrapped vans. Our website is at www.trvadvisory.example and our primary colors are the orange, green, grey and blue all military color finishes.

We are interesting in the slogans "Pairing You with the Right Technology" or "Leading the Lowcountry in Tech"

Target Market(s)

We focus on 70% Commercial and 30% Residential Customers

Industry/Entity Type

Low Voltage, AV Company

Contact Information for Business Card

Name - Dorian Fairweather, Title - Owner, Office Phone - 555-714-3096, Mobile Phone - 555-802-4173, E-Mail - d@trvadvisory.example, Website: www.trvadvisory.example

Font styles to use
Sans Serif

Requirements
Must have
• Must have Name, Title, Work Phone & Mobile, Website and Logo.
Nice to have
• We want something that will impress our higher end clients with a great logo
Should not have
• Too traditional or plain.

```html
<!DOCTYPE html>
<html lang="en">
<head>
<meta charset="utf-8">
<title>TR Advisory Business Card</title>
<link rel="stylesheet" href="https://fonts.googleapis.com/css2?family=Mulish:wght@500;600;700;800&display=swap">
<style>
  :root {
    --page-bg: #e9e9e9;
    --orange: #e8590c;
    --orange-light: #f0700f;
    --orange-deep: #d94c05;
    --maroon: #530c00;
    --ink-light: #f3ece8;
    --strip-edge: #f2300c;
  }
  * { box-sizing: border-box; margin: 0; padding: 0; }
  html, body {
    width: 1200px; height: 900px; overflow: hidden;
    background: var(--page-bg);
    font-family: "Mulish", sans-serif;
  }
  .card {
    position: absolute; left: 100px; top: 164px;
    width: 1000px; height: 572px;
    display: flex;
    box-shadow: 0 10px 30px rgba(0,0,0,0.18);
  }
  .card__brand {
    width: 502px; height: 100%;
    background: linear-gradient(160deg, var(--orange-light) 0%, var(--orange) 55%, var(--orange-deep) 100%);
    display: flex; align-items: center; justify-content: center;
  }
  .brand-name {
    color: var(--maroon);
    font-weight: 800;
    font-size: 52px;
    letter-spacing: 1px;
  }
  .card__info {
    position: relative; flex: 1; height: 100%;
    background: var(--maroon);
    color: var(--ink-light);
  }
  .person {
    position: absolute; right: 67px; top: 48px;
    text-align: right;
  }
  .person__name { font-size: 31px; font-weight: 600; line-height: 1.2; }
  .person__title { font-size: 23px; font-weight: 500; margin-top: 2px; }
  .icon-strip {
    position: absolute; left: 1px; top: 216px;
    width: 72px; height: 292px;
    background: linear-gradient(90deg, var(--orange) 0%, var(--orange-light) 70%, var(--strip-edge) 100%);
  }
  .icon {
    position: absolute; left: 21px; width: 30px; height: 30px;
    fill: none; stroke: var(--maroon); stroke-width: 1.8;
    stroke-linecap: round; stroke-linejoin: round;
  }
  .contact {
    position: absolute; left: 94px;
    font-weight: 600; line-height: 1;
  }
  .contact--phone { font-size: 27px; }
  .contact--web { font-size: 24px; }
</style>
</head>
<body>
  <div class="card">
    <div class="card__brand" role="img" aria-label="Orange circuit-board pattern background behind the company name">
      <span class="brand-name">TR Advisory</span>
    </div>
    <div class="card__info">
      <div class="person">
        <div class="person__name">Dorian Fairweather</div>
        <div class="person__title">(Owner)</div>
      </div>

      <div class="icon-strip">
        <svg class="icon" style="top:44px" viewBox="0 0 24 24" aria-hidden="true">
          <path d="M5 3h4l2 5-2.5 1.5a11 11 0 0 0 6 6L16 13l5 2v4a2 2 0 0 1-2 2A17 17 0 0 1 3 5a2 2 0 0 1 2-2z"/>
        </svg>
        <svg class="icon" style="top:102px" viewBox="0 0 24 24" aria-hidden="true">
          <rect x="6" y="2" width="12" height="20" rx="2"/>
          <line x1="6" y1="5" x2="18" y2="5"/>
          <line x1="6" y1="18" x2="18" y2="18"/>
        </svg>
        <svg class="icon" style="top:161px" viewBox="0 0 24 24" aria-hidden="true">
          <rect x="2" y="5" width="20" height="14"/>
          <path d="M2 5l10 8 10-8M2 19l7.5-7M22 19l-7.5-7"/>
        </svg>
        <svg class="icon" style="top:219px" viewBox="0 0 24 24" aria-hidden="true">
          <circle cx="12" cy="12" r="10"/>
          <ellipse cx="12" cy="12" rx="4.5" ry="10"/>
          <line x1="2" y1="12" x2="22" y2="12"/>
          <path d="M4 7h16M4 17h16"/>
        </svg>
      </div>

      <div class="contact contact--phone" style="top:262px">555-714-3096</div>
      <div class="contact contact--phone" style="top:320px">555-802-4173</div>
      <div class="contact contact--web" style="top:380px">d@trvadvisory.example</div>
      <div class="contact contact--web" style="top:438px">www.trvadvisory.example</div>
    </div>
  </div>
</body>
</html>
```